Website for Brisbeck Current Glide

Require a website for a river float in the City of Edmonton. Located on North Saskatchewan River. Will need to be a coded website with incorporated booking system through Fare Harbor software.

Pages include
Home
Pricing
About
FAQ
Contact

Brisbeck Current Glide is an activity based business that will have customers floating down the North Saskatchewan river in Edmonton AB. The site will have all information needed and a full reservation system. The project was launched to provide people in the Edmonton area a favorite summer activity.

Here are similar websites to reference what our business will be doing and what we are looking for.

mellowbendcanoehire.example
pinegulchloopers.example

Target Market(s)

Families, Groups, Individuals, Anyone who wants to explore the river

Industry/Entity Type

Activities based business/ Outdoor recreational/ River Float

Coding

Coded - Design and coding required

Number of Pages Required

5+ page

Colors
0054AA
0677BA
7BADD7
CADEEF
E8F1F8
F0912C
F2A743
F7CA91
FBE8D2
FDF5EE

```html
<!DOCTYPE html>
<html lang="en">
<head>
<meta charset="utf-8">
<title>Brisbeck Current Glide — Website Screens</title>
<link href="https://fonts.googleapis.com/css2?family=Bitter:wght@400;700;800&family=Hind:wght@700&family=Roboto:wght@400;700&display=swap" rel="stylesheet">
<style>
:root{
  --board:#2163a5;
  --orange:#ff4d00;
  --orange-2:#ff8a00;
  --amber:#f7931e;
  --blue:#2b8cf0;
  --blue-deep:#1c6fd0;
  --blue-pale:#7badd7;
  --white:#ffffff;
  --ink-dark:#26313a;
}
*{margin:0;padding:0;box-sizing:border-box}
html,body{width:1200px;height:849px;overflow:hidden;background:var(--board)}
body{position:relative;font-family:"Bitter",serif;color:var(--white)}
.a{position:absolute}
.c{left:0;right:0;text-align:center}
.label{font-family:"Hind",sans-serif;font-weight:700;font-size:18px;top:56px;line-height:1}
.screen{position:absolute;top:91px;height:675px;overflow:hidden;background:var(--orange)}
.btn{position:absolute;display:flex;align-items:center;justify-content:center;font-family:"Roboto",sans-serif;font-size:3.6px;color:var(--white);background:var(--orange)}
.btn.blue{background:var(--blue)}
.btn.grad{background:linear-gradient(90deg,var(--orange),var(--orange-2))}
.photo-city{background:linear-gradient(180deg,#4a5560 0%,#3c4a3f 45%,#2c3a2c 70%,#1e2a2c 100%)}
.photo-blue{background:linear-gradient(180deg,#5aa0e6 0%,#3d86d6 45%,#2b74c8 100%)}
.photo-river{background:linear-gradient(180deg,#8c8a76 0%,#6a7b70 22%,#2f5f86 40%,#24547c 100%)}
.photo-floats{background:linear-gradient(135deg,#1d3a40 0%,#c05a3a 35%,#2c8aa0 60%,#1c3036 100%)}
.hl{color:var(--amber)}
.outline{color:var(--blue);-webkit-text-stroke:.2px #cfe6ff}
.dot{position:absolute;border-radius:50%;background:var(--orange);border:1px solid var(--white)}
.dot::after{content:"";position:absolute;left:50%;top:50%;width:40%;height:40%;transform:translate(-50%,-50%) rotate(45deg);border-top:1.2px solid var(--white);border-right:1.2px solid var(--white)}
.brand{font-family:"Bitter",serif;font-weight:700;color:var(--white);font-size:2.6px;white-space:nowrap}
.sq{display:inline-block;width:7px;height:7px;background:var(--blue);border:.6px solid var(--white);margin-right:2px}
.field{position:absolute;height:8px;border-radius:4px;background:var(--blue);border:.5px solid var(--white);font-family:"Roboto",sans-serif;font-size:2.6px;padding-left:3px;line-height:7px}
.card{position:absolute;background:var(--white);text-align:center}
.bar{position:absolute;height:1px;background:var(--white)}
</style>
</head>
<body>

<div class="a label" style="left:164px">Desktop</div>
<div class="a label" style="left:513px">Desktop</div>
<div class="a label" style="left:891px">Mobile</div>

<!-- Screen one: home -->
<section class="screen" style="left:159px;width:297px">
  <header class="a" style="left:0;top:0;width:297px;height:21px;background:linear-gradient(90deg,var(--orange),var(--orange-2))">
    <span class="a" style="left:34px;top:4px;width:8px;height:8px;border-radius:50%;background:var(--blue-pale)"></span>
    <span class="a brand" style="left:28px;top:13px">BRISBECK</span>
    <nav class="a" style="left:173px;top:8px;font-family:Roboto,sans-serif;font-weight:700;font-size:3.4px;word-spacing:3px">HOME PRICING ABOUT FAQ CONTACT</nav>
  </header>
  <div class="a photo-city" role="img" aria-label="Evening view of the Edmonton skyline over the river valley" style="left:0;top:21px;width:297px;height:129px"></div>
  <span class="dot" style="left:140px;top:44px;width:16px;height:16px"></span>
  <p class="a c" style="top:60px;font-size:5.6px">Edmonton’s Best Summer Activity</p>
  <h1 class="a c" style="top:69px;font-size:13px;font-weight:700;white-space:nowrap"><span class="hl">BRISBECK</span> CURRENT GLIDE</h1>
  <p class="a c" style="top:88px;font-size:8.2px;line-height:9.6px">Float the North Saskatchewan<br>through downtown Edmonton</p>
  <span class="btn grad" style="left:124px;top:113px;width:49px;height:13px">BOOK NOW...</span>

  <div class="a photo-blue" role="img" aria-label="River valley and skyline in a blue tint" style="left:0;top:150px;width:297px;height:135px"></div>
  <h2 class="a c" style="top:158px;font-size:12.5px;font-weight:700"><span class="hl">OUR</span> PRICING</h2>
  <div class="card" style="left:50px;top:184px;width:196px;height:69px;border-radius:8px">
    <p style="margin-top:4px;font-size:5.6px;font-weight:700;color:var(--orange)">$30/person ALL INCLUSIVE FEE</p>
    <p style="margin-top:4px;font-size:4px;color:var(--blue)">We keep our pricing simple and include everything you need:</p>
    <p style="margin-top:4px;font-size:4px;line-height:5.6px;color:var(--amber)">Premium comfort float tube with backrest and cup holder<br>Lifejacket<br>Paddle<br>Round trip shuttle service<br>Safety training<br>Staff assistance<br>Parking<br>Unlimited Fun!</p>
  </div>
  <span class="btn grad" style="left:124px;top:263px;width:49px;height:13px">BOOK NOW...</span>

  <div class="a" style="left:0;top:279px;width:297px;height:140px;background:var(--orange);clip-path:polygon(0 10px,100% 0,100% 100%,0 100%)"></div>
  <h3 class="a outline" style="left:22px;top:318px;font-size:8px;line-height:10.5px;font-weight:700">SHUTTLE SERVICE<br>AND GEAR INCLUDED</h3>
  <p class="a" style="left:22px;top:343px;width:110px;font-size:4.8px;line-height:7px">We provide everything you need including round trip shuttle service, float tube, lifejacket, paddle, and more. Fun for everyone!</p>
  <span class="btn blue" style="left:22px;top:377px;width:39px;height:9px">BOOK NOW...</span>
  <div class="a photo-river" role="img" aria-label="Many colourful float tubes drifting down the river" style="left:142px;top:315px;width:113px;height:75px"></div>

  <div class="a photo-blue" role="img" aria-label="Downtown skyline and arched bridge in a blue tint" style="left:0;top:412px;width:297px;height:122px;clip-path:polygon(0 12px,100% 0,100% 100%,0 100%)"></div>
  <p class="a c" style="top:445px;font-size:5.6px">Enjoy Summer With Us.</p>
  <h2 class="a c" style="top:459px;font-size:12.5px;font-weight:700">VISIT OUR RIVER FLOAT</h2>
  <span class="btn grad" style="left:124px;top:478px;width:49px;height:13px">BOOK NOW...</span>

  <div class="a" style="left:0;top:522px;width:297px;height:153px;background:var(--orange);clip-path:polygon(0 11px,100% 0,100% 100%,0 100%)"></div>
  <div class="a photo-floats" role="img" aria-label="Overhead view of friends on inflatable floats" style="left:17px;top:560px;width:129px;height:70px"></div>
  <h3 class="a outline" style="left:152px;top:564px;font-size:8px;line-height:11.5px;font-weight:700">FLOATING<br>7 DAYS A WEEK</h3>
  <p class="a" style="left:152px;top:593px;width:128px;font-size:4.8px;line-height:5.2px">Our priority is to make sure everyone has a safe and fun time on the river. Safety demonstrations are provided and staff are available to assist in any way. Whether you are a family with children, larger group or just want a relaxing way to explore the river, this is a must try activity.</p>
  <span class="btn blue" style="left:152px;top:628px;width:41px;height:10px;font-size:3.8px">BOOK NOW...</span>
</section>

<!-- Screen two: about, FAQ, contact -->
<section class="screen" style="left:513px;width:324px">
  <div class="a photo-blue" role="img" aria-label="Aerial view of the river valley and skyline in a blue tint" style="left:0;top:0;width:324px;height:133px;clip-path:polygon(0 16px,100% 6px,100% 122px,0 133px)"></div>
  <p class="a c" style="top:49px;font-size:6.2px">For the Love of Fun and the Outdoors</p>
  <h1 class="a c" style="top:63px;font-size:14.5px;font-weight:700;white-space:nowrap"><span class="hl">365, 24/7</span> All Day Any Day Fun</h1>
  <span class="btn grad" style="left:137px;top:85px;width:53px;height:15px">BOOK NOW...</span>

  <p class="a c" style="top:140px;font-size:6.2px">What are we all about?</p>
  <h2 class="a c outline" style="top:152px;font-size:13.5px;font-weight:800">About Us</h2>
  <span class="bar" style="left:152px;top:168px;width:20px;height:1.4px"></span>
  <h2 class="a c" style="top:180px;font-size:14.5px;font-weight:400">Edmonton’s Best Summer Activity</h2>
  <p class="a c" style="top:198px;font-size:7.2px">Float the North Saskatchewan through downtown Edmonton</p>
  <div class="a" style="left:0;top:218px;width:324px;height:69px;overflow:hidden">
    <p class="a" style="left:39px;top:0;width:98px;text-align:right;font-size:5px;line-height:6px">We provide the lifejacket, paddle, river tube and shuttle service. You just have to show up. Brisbeck Current Glide was launched to provide people in the Edmonton area a favorite summer activity.<br><br>Nothing is better on a hot summer day, than spending it on the river and seeing Edmonton from a new perspective. Our home base and meeting spot is at Millcreek Landing.</p>
    <span class="a" style="left:151px;top:24px;width:24px;height:24px;border-radius:50%;background:var(--blue-pale)"></span>
    <span class="a brand" style="left:145px;top:50px;font-size:3.4px">BRISBECK</span>
    <p class="a" style="left:188px;top:0;width:100px;font-size:5px;line-height:6px">This is where you will check in, and board the shuttle. The shuttle will take all floaters up river to Hollins Park Boat Launch, where your tube will be waiting. Once on the river, you can sit back, relax, explore and enjoy the view.<br><br>Once you complete the float, and arrive back at Millcreek Landing, staff will be available to assist in exiting the river where you will return your tube and gear.</p>
  </div>

  <div class="a" style="left:0;top:286px;width:324px;height:154px;background:var(--white);clip-path:polygon(0 7px,100% 0,100% 100%,0 100%)"></div>
  <p class="a c" style="top:306px;font-size:6.2px;color:var(--orange)">What you need to know!</p>
  <h2 class="a c" style="top:316px;font-size:14.5px;font-weight:700;color:var(--blue)">FAQ</h2>
  <h3 class="a c" style="top:338px;font-size:10.5px;font-weight:700;color:var(--blue)">How do I reserve my float?</h3>
  <p class="a c" style="top:357px;font-size:5.2px;line-height:6.6px;color:var(--blue)">We highly recommend booking online, as we do sell out. BOOK NOW<br>Floats can also be reserved on-site at Millcreek Landing, on a first come first serve basis.</p>
  <h3 class="a c" style="top:373px;font-size:10.5px;font-weight:700;color:var(--amber)">What safety information should I know?</h3>
  <p class="a" style="left:43px;top:391px;width:238px;text-align:center;font-size:5.2px;line-height:6.4px;color:var(--amber)">Children 12 years and younger should be accompanied by an adult at all times on the river. Life jackets and paddles are provided and are recommended for everyone, especially if you are a weak or inexperienced swimmer. You must exit the river at the designated exit point (Millcreek Landing) and are responsible for doing so. There are no lifeguards on site, and all floaters enter and exit the river at their own risk. Staff safety demonstration is provided before entering the river. All non-swimmers and anyone not comfortable around open water should not float the North Saskatchewan.</p>

  <p class="a c" style="top:456px;font-size:6.2px">We’d love to hear from You!</p>
  <h2 class="a c outline" style="top:466px;font-size:13.5px;font-weight:800">Contact Us</h2>
  <span class="bar" style="left:152px;top:484px;width:20px;height:1.4px"></span>
  <p class="a" style="left:36px;top:508px;font-size:5.2px;line-height:6.2px">Come visit us on float days at Millcreek Landing<br>4410 Alder Row NW, Edmonton, AB <i>Map</i></p>
  <div class="a" style="left:36px;top:525px;line-height:0"><span class="sq"></span><span class="sq"></span><span class="sq"></span></div>
  <span class="field" style="left:166px;top:507px;width:123px">Name</span>
  <span class="field" style="left:166px;top:518px;width:123px">E-mail</span>
  <span class="field" style="left:166px;top:530px;width:123px">Message</span>
  <span class="btn blue" style="left:166px;top:544px;width:40px;height:7px;border-radius:4px;font-size:2.8px;font-weight:700">Send message</span>

  <footer class="a" style="left:0;top:584px;width:324px;height:91px;background:var(--blue);clip-path:polygon(0 14px,100% 0,100% 100%,0 100%)">
    <div class="a" style="left:36px;top:23px;font-size:2.6px;line-height:5.3px"><b>NAVIGATE</b><br>HOME<br>PRICING<br>ABOUT<br>FAQ<br>CONTACT</div>
    <div class="a" style="left:122px;top:23px;font-size:2.6px;line-height:5.3px"><b>FOLLOW US</b><br>Circlewall<br>Snapgrid<br>Worklink<br>Chirpline</div>
    <div class="a" style="left:122px;top:50px;line-height:0"><span class="sq" style="width:8px;height:8px"></span><span class="sq" style="width:8px;height:8px"></span><span class="sq" style="width:8px;height:8px"></span><span class="sq" style="width:8px;height:8px"></span></div>
    <div class="a" style="left:208px;top:23px;font-size:2.6px;line-height:5.3px"><b>CONTACT</b><br>EMAIL: info@brisbeckcurrentglide.example</div>
    <p class="a c" style="top:80px;font-size:2.6px"><b>© Brisbeck Current Glide 2022.</b> All Rights Reserved.</p>
  </footer>
</section>

<!-- Screen three: mobile home -->
<section class="screen" style="left:891px;width:88px">
  <header class="a" style="left:0;top:0;width:88px;height:42px;background:linear-gradient(90deg,var(--orange),var(--orange-2))">
    <span class="a" style="left:38px;top:4px;width:12px;height:12px;border-radius:50%;background:var(--blue-pale)"></span>
    <span class="a brand" style="left:32px;top:18px;font-size:3px">BRISBECK</span>
    <svg class="a" style="left:74px;top:31px" width="6" height="5" viewBox="0 0 6 5"><path d="M0 .5h6M0 2.5h6M0 4.5h6" stroke="#fff" stroke-width=".7"/></svg>
  </header>
  <div class="a photo-city" role="img" aria-label="Evening view of the Edmonton skyline" style="left:0;top:42px;width:88px;height:109px"></div>
  <span class="dot" style="left:33px;top:54px;width:22px;height:22px"></span>
  <p class="a c" style="top:77px;font-size:6.2px">Edmonton’s Best</p>
  <span class="bar" style="left:10px;top:87px;width:68px;height:.5px;background:var(--amber)"></span>
  <h1 class="a c" style="top:88px;font-size:6.8px;line-height:10px;font-weight:700"><span class="hl">BRISBECK</span> CURRENT<br>GLIDE</h1>
  <p class="a c" style="top:109px;font-size:4.6px;line-height:5.8px">Float the North Saskatchewan<br>through downtown Edmonton</p>
  <span class="btn grad" style="left:20px;top:134px;width:48px;height:13px">BOOK NOW...</span>

  <div class="a photo-blue" role="img" aria-label="River valley in a blue tint" style="left:0;top:151px;width:88px;height:202px;clip-path:polygon(0 0,100% 0,100% 189px,0 202px)"></div>
  <h2 class="a c" style="top:157px;font-size:13.5px;line-height:20px;font-weight:700"><span class="hl">OUR</span><br>PRICING</h2>
  <div class="card" style="left:4px;top:206px;width:79px;height:106px;border-radius:10px">
    <p style="margin-top:8px;font-size:5.8px;line-height:8px;font-weight:700;color:var(--orange)">$30/person ALL<br>INCLUSIVE FEE</p>
    <p style="margin-top:4px;font-size:4.2px;line-height:5px;color:var(--blue)">We keep our pricing simple<br>and include everything you<br>need:</p>
    <p style="margin-top:5px;font-size:4.2px;line-height:5.3px;color:var(--amber)">Premium comfort float tube with<br>backrest and cup holder<br>Lifejacket<br>Paddle<br>Round trip shuttle service<br>Safety training<br>Staff assistance<br>Parking<br>Unlimited Fun!</p>
  </div>
  <span class="btn grad" style="left:22px;top:327px;width:42px;height:20px">BOOK NOW...</span>

  <h3 class="a c outline" style="top:370px;font-size:5.3px;line-height:8px;font-weight:700">SHUTTLE SERVICE<br>AND GEAR INCLUDED</h3>
  <p class="a c" style="top:392px;font-size:3.2px;line-height:6.4px">We provide everything you need including<br>round trip shuttle service, float tube,<br>lifejacket, paddle, and more. Fun for everyone!</p>
  <span class="btn blue" style="left:18px;top:423px;width:50px;height:11px">BOOK NOW...</span>
  <div class="a photo-river" role="img" aria-label="Float tubes drifting down the river" style="left:3px;top:447px;width:81px;height:53px"></div>

  <div class="a photo-blue" role="img" aria-label="Skyline and arched bridge in a blue tint" style="left:0;top:512px;width:88px;height:150px;clip-path:polygon(0 13px,100% 0,100% 133px,0 149px)"></div>
  <p class="a c" style="top:533px;font-size:6.2px">Enjoy Summer With Us.</p>
  <h2 class="a c" style="top:552px;font-size:13.5px;line-height:19.5px;font-weight:800">VISIT OUR<br>RIVER<br>FLOAT</h2>
  <span class="btn grad" style="left:8px;top:620px;width:70px;height:20px">BOOK NOW...</span>
</section>

</body>
</html>
```